we need a homepage for a marketplace

We manage all projects using our ground-breaking platform Kelvrim Hub. You get access to 150+ partners in 70 countries, security, cost efficiency, technical skills, speed, 100% visibility and accountability.Kelvrim aims to help clients realize the full potential of their investments, provide a competitive price, establish the business need as a competitive advantage, and provide a strategic business asset that can facilitate growth.
Target Market(s)
Freelancers
Industry/Entity Type
Business Software
Number of Pages Required
1 page
Requirements
Must have
- Credentials -http://qabdel.example/freelancer/public
- Front :
- Client:
- Email id - tomasp@lurvantsystems.example
- Password - 908172
- Partner:
- Email id - dorian@lurvantsystems.example
- Password - 908172
- Project Manager:
- Email id - mirela@lurvantsystems.example
- Password - 908172
Nice to have
- It will be nice to have a creative design, and a outside the box look/feel

```html
<!DOCTYPE html>
<html lang="en">
<head>
<meta charset="utf-8">
<title>Kelvrim — Marketplace Home</title>
<link href="https://fonts.googleapis.com/css2?family=Playfair+Display:wght@400;700&family=Roboto:wght@300;400;500;700&display=swap" rel="stylesheet">
<style>
:root{
  --orange:#f0641e;
  --blue:#3b9fc4;
  --teal:#4ea6bf;
  --navy:#2b4a66;
  --ink:#2b2b2b;
  --grey-text:#666;
  --light:#ececec;
  --dark:#2f3136;
  --white:#fff;
  --line:#dcdcdc;
}
*{box-sizing:border-box;margin:0;padding:0}
html,body{width:1200px;height:3913px;overflow:hidden}
body{position:relative;font-family:'Roboto',sans-serif;color:var(--ink);background:var(--white)}
section,header,footer{position:absolute;left:0;width:1200px}
.serif{font-family:'Playfair Display',serif}

.topbar{top:0;height:36px}
.topbar .social{position:absolute;left:73px;top:6px;display:flex;gap:7px}
.dot{width:24px;height:24px;border-radius:50%;background:#3a3a3a}
.topbar .contact{position:absolute;left:245px;top:9px;font-size:14px;color:#444;display:flex;gap:26px}
.topbar .auth{position:absolute;right:73px;top:2px;display:flex;gap:8px}
.auth span{display:block;height:34px;line-height:34px;padding:0 16px;color:#fff;font-size:14px;font-weight:500}
.btn-login{background:var(--blue)}
.btn-add{background:var(--orange)}

.nav{top:36px;height:107px}
.logo{position:absolute;left:73px;top:30px;font-size:40px;font-weight:500;color:var(--navy)}
.nav ul{position:absolute;right:73px;top:50px;list-style:none;display:flex;gap:26px;font-size:14px;font-weight:500;color:#333}

.hero{top:143px;height:608px;background:linear-gradient(120deg,#3f3a36,#6a6460 45%,#2c2b2c)}
.hero-banner{position:absolute;left:0;top:212px;width:610px;height:160px;background:rgba(66,104,140,.85);padding:24px 20px 0 73px;font-size:29px;font-weight:300;line-height:41px;color:#fff}
.hero-btns{position:absolute;left:73px;top:486px;display:flex;gap:8px}
.hero-btns span{display:flex;align-items:center;gap:14px;height:48px;padding:0 22px;color:#fff;font-size:15px;font-weight:500}
.hb-partner{background:var(--teal)}
.hb-post{background:var(--orange)}

.about{top:751px;height:327px;background:var(--light);text-align:center}
.about h2{margin-top:68px;font-size:32px;font-weight:400}
.about p{margin:22px auto 0;width:830px;font-size:21px;line-height:32px;color:#555;font-weight:300}
.btn-outline{display:inline-block;margin-top:22px;border:2px solid #444;padding:9px 22px;font-size:15px;color:#333}

.how{top:1078px;height:652px;text-align:center}
.how h2{margin-top:68px;font-size:32px;font-weight:400}
.how .sub{margin-top:10px;font-size:16px;color:#555}
.steps{position:absolute;left:73px;top:177px;width:1054px;display:flex}
.step{flex:1;border-right:1px solid var(--line);height:400px;text-align:left;padding:0 12px}
.step:last-child{border-right:none}
.step-art{height:205px;background:linear-gradient(135deg,#eef6fb,#fde9d6)}
.step-head{display:flex;justify-content:space-between;align-items:center;margin-top:22px}
.step h3{font-size:17px;font-weight:500;line-height:18px;color:#222}
.step p{margin-top:22px;font-size:14px;line-height:22px;color:#555}

.industries{top:1730px;height:756px;background:linear-gradient(100deg,#2a2a2a,#3b3835 55%,#26292c)}
.industries h2{text-align:center;margin-top:70px;font-size:32px;line-height:34px;font-weight:700;color:#fff}
.grid{position:absolute;left:73px;top:185px;width:1054px;display:grid;grid-template-columns:repeat(4,1fr);row-gap:34px}
.svc{padding-right:28px;color:#fff}
.svc h3{margin-top:12px;font-size:17px;font-weight:700;line-height:18px}
.svc p{margin-top:16px;font-size:14px;line-height:22px;color:#ddd}

.subscribe{top:2486px;height:162px;background:var(--teal)}
.sub-title{position:absolute;left:73px;top:30px;font-size:27px;line-height:30px;color:var(--navy)}
.sub-text{position:absolute;left:315px;top:28px;width:640px;font-size:15px;line-height:20px;color:#fff}
.sub-form{position:absolute;left:315px;top:86px;display:flex;gap:8px}
.field{width:300px;height:42px;background:#fff;line-height:42px;padding-left:12px;font-size:14px;color:#555}
.sub-btn{width:196px;height:42px;background:#1f3a52;color:#fff;text-align:center;line-height:42px;font-weight:700;font-size:15px}

.partners{top:2648px;height:566px;text-align:center}
.partners h2{margin-top:70px;font-size:32px;font-weight:400}
.cards{position:absolute;left:73px;top:146px;display:flex;gap:23px}
.card{width:246px;height:285px;background:#ececec;text-align:left;padding:10px}
.photo{height:152px;background:linear-gradient(180deg,#d9dde3,#8e9aa8)}
.card dl{margin-top:14px;font-size:14px;line-height:26px;color:#333}
.pager{position:absolute;left:562px;top:470px;display:flex;gap:8px}
.pager span{width:34px;height:34px;border:2px solid #555;display:flex;align-items:center;justify-content:center}

.talent{top:3214px;height:300px;background:var(--light);text-align:center}
.talent h2{margin-top:68px;font-size:32px;font-weight:700}
.talent p{margin-top:8px;font-size:17px;color:#555}
.btn-register{display:inline-flex;align-items:center;gap:14px;margin-top:32px;height:50px;padding:0 28px;background:var(--teal);color:#fff;font-size:15px;font-weight:500}

.footer{top:3514px;height:399px;background:var(--dark);color:#fff}
.fcol{position:absolute;top:42px}
.fcol h4{font-size:15px;font-weight:700;margin-bottom:10px}
.fcol li{list-style:none;font-size:12px;line-height:22px;color:#9aa0a8}
.fsocial{position:absolute;right:73px;top:40px;display:flex;gap:10px}
.fsocial .dot{width:34px;height:34px;background:transparent;border:2px solid #888}
.fcontact{position:absolute;left:725px;top:158px;display:flex;gap:48px;font-size:14px;color:#9fc3e3;text-align:center}
.fcontact div{display:flex;flex-direction:column;align-items:center;gap:8px}
.ic{width:34px;height:34px;border-radius:50%;background:#ddd}
.flogo{position:absolute;right:73px;top:312px;font-size:42px;font-weight:500;color:#fff}
.fbottom{position:absolute;left:73px;top:356px;font-size:13px;color:#9aa0a8}
</style>
</head>
<body>

<header class="topbar">
  <div class="social"><span class="dot"></span><span class="dot"></span><span class="dot"></span><span class="dot"></span><span class="dot"></span></div>
  <div class="contact"><span>☎ 02531478096</span><span>✉ info@kelvrim.example</span></div>
  <div class="auth"><span class="btn-login">LOGIN</span><span class="btn-add">+ ADD PROJECT</span></div>
</header>

<header class="nav">
  <div class="logo">Kelvrim</div>
  <ul><li>ABOUT US</li><li>HOW IT WORKS</li><li>BROWSE PROJECT MANAGER</li></ul>
</header>

<section class="hero" role="img" aria-label="Photo of hands holding a tablet showing business charts">
  <div class="hero-banner">Aiming To Provide Faster, Smarter And Cheaper Solutions And Services Assuring Rapid Growth Of Technology.</div>
  <div class="hero-btns">
    <span class="hb-partner"><svg width="24" height="18" viewBox="0 0 24 18"><path d="M2 9l6-6 4 3 4-3 6 6-8 7z" fill="none" stroke="#fff" stroke-width="2"/></svg>BECOME A PARTNER</span>
    <span class="hb-post"><svg width="26" height="26" viewBox="0 0 26 26"><circle cx="13" cy="13" r="12" fill="#fff"/><path d="M13 7v12M7 13h12" stroke="#f0641e" stroke-width="3"/></svg>POST YOUR PROJECT</span>
  </div>
</section>

<section class="about">
  <h2 class="serif">ABOUT KH</h2>
  <p>We are experienced and highly qualified software engineers, cloud architects, inventors, cyber security engineers and project managers.</p>
  <span class="btn-outline">Learn More</span>
</section>

<section class="how">
  <h2 class="serif">HOW IT WORKS</h2>
  <p class="sub">Organizations Can Benefit From Our Talent Pool In The Following East Steps</p>
  <div class="steps">
    <div class="step"><div class="step-art" role="img" aria-label="Illustration of posting a project online"></div><div class="step-head"><h3>POST YOUR<br>PROJECT</h3><svg width="30" height="26"><path d="M2 2l26 12-26 10z" fill="#1a9b3a"/></svg></div><p>Lorem ipsum dolor sit amet, consectetuer adipiscing elit, sed diam nonummy nibh euismod tincidunt</p></div>
    <div class="step"><div class="step-art" role="img" aria-label="Illustration of selecting an expert"></div><div class="step-head"><h3>SELECT AN<br>EXPERT</h3><svg width="30" height="26"><path d="M2 2l26 12-26 10z" fill="#1a9b3a"/></svg></div><p>Lorem ipsum dolor sit amet, consectetuer adipiscing elit, sed diam nonummy nibh euismod tincidunt</p></div>
    <div class="step"><div class="step-art" role="img" aria-label="Illustration of working on the project"></div><div class="step-head"><h3>WORK ON<br>THE PROJECT</h3><svg width="30" height="26"><path d="M2 2l26 12-26 10z" fill="#1a9b3a"/></svg></div><p>Lorem ipsum dolor sit amet, consectetuer adipiscing elit, sed diam nonummy nibh euismod tincidunt</p></div>
    <div class="step"><div class="step-art" role="img" aria-label="Illustration of paying when satisfied"></div><div class="step-head"><h3>PAY ONLY WHEN<br>SATISFIED</h3><svg width="30" height="26"><path d="M2 2l26 12-26 10z" fill="#1a9b3a"/></svg></div><p>Lorem ipsum dolor sit amet, consectetuer adipiscing elit, sed diam nonummy nibh euismod tincidunt</p></div>
  </div>
</section>

<section class="industries" role="region" aria-label="Industries served, over a photo of a team meeting">
  <h2 class="serif">PROJECT MANAGER FOR EVERY BUSINESS<br>CHALLENGE ACROSS A WIDE RANGE OF INDUSTRIES</h2>
  <div class="grid">
    <div class="svc"><svg width="44" height="44"><circle cx="22" cy="22" r="21" fill="#1e1e1e" stroke="#555"/><path d="M13 26h18a5 5 0 0 0-3-9 7 7 0 0 0-13 2 4 4 0 0 0-2 7z" fill="none" stroke="#f0641e" stroke-width="2"/></svg><h3>CLOUD<br>COMPUTING</h3><p>Locate your system in the cloud and access your information from any place or device with the highest security level....</p></div>
    <div class="svc"><svg width="44" height="44"><circle cx="22" cy="22" r="21" fill="#1e1e1e" stroke="#555"/><rect x="14" y="12" width="16" height="20" fill="none" stroke="#f0641e" stroke-width="2"/><path d="M17 22l3 3 6-6" fill="none" stroke="#f0641e" stroke-width="2"/></svg><h3>QA<br>TESTING</h3><p>We will help you find and eliminate problems &amp; bugs, enhance performance of your product and give another brush to logics and design....</p></div>
    <div class="svc"><svg width="44" height="44"><circle cx="22" cy="22" r="21" fill="#1e1e1e" stroke="#555"/><circle cx="22" cy="15" r="3" fill="#f0641e"/><circle cx="15" cy="27" r="3" fill="#f0641e"/><circle cx="29" cy="27" r="3" fill="#f0641e"/></svg><h3>CONSULTING<br>SERVICES</h3><p>Should you need a consultation, training, troubleshooting or implementation of enhancements to your product, our team is always ready to help you!...</p></div>
    <div class="svc"><svg width="44" height="44"><circle cx="22" cy="22" r="21" fill="#1e1e1e" stroke="#555"/><rect x="12" y="13" width="20" height="15" fill="none" stroke="#f0641e" stroke-width="2"/><path d="M18 32h8" stroke="#f0641e" stroke-width="2"/></svg><h3>WEB<br>DEVELOPMENT</h3><p>Our goal is to bring the most recognizable and modern solutions to the world web market. We do our best in order to make your site usable, profitable and, what....</p></div>
    <div class="svc"><svg width="44" height="44"><circle cx="22" cy="22" r="21" fill="#1e1e1e" stroke="#555"/><rect x="12" y="13" width="20" height="15" fill="none" stroke="#f0641e" stroke-width="2"/><path d="M17 24l8-8" stroke="#f0641e" stroke-width="2"/></svg><h3>WEB<br>DESIGN</h3><p>Our passion, dedication and your idea blend in elegant customized design that turns your project into success....</p></div>
    <div class="svc"><svg width="44" height="44"><circle cx="22" cy="22" r="21" fill="#1e1e1e" stroke="#555"/><rect x="15" y="20" width="14" height="11" fill="none" stroke="#f0641e" stroke-width="2"/><path d="M18 20v-4a4 4 0 0 1 8 0v4" fill="none" stroke="#f0641e" stroke-width="2"/></svg><h3>SECURITY &amp;<br>COMPLIANCE</h3><p>Protect your information with best of our data security methods and techniques and build the trust of your customers!...</p></div>
    <div class="svc"><svg width="44" height="44"><circle cx="22" cy="22" r="21" fill="#1e1e1e" stroke="#555"/><rect x="16" y="11" width="12" height="22" rx="2" fill="none" stroke="#f0641e" stroke-width="2"/></svg><h3>MOBILE APP<br>DEVELOPMENT</h3><p>But I must explain to you how all this mistaken idea of denouncing pleasure and praising pain was born and I will give you a complete account of the system, and...</p></div>
    <div class="svc"><svg width="44" height="44"><circle cx="22" cy="22" r="21" fill="#1e1e1e" stroke="#555"/><path d="M13 24v-3a9 9 0 0 1 18 0v3" fill="none" stroke="#f0641e" stroke-width="2"/><rect x="12" y="23" width="5" height="7" fill="#f0641e"/><rect x="27" y="23" width="5" height="7" fill="#f0641e"/></svg><h3>TECHNICAL SUPPORT<br>SERVICES</h3><p>Outstaffing development teams is what nowadays makes IT one of the most scalable industries. We are not saying that traditional inhouse teams are replaced by fr...</p></div>
  </div>
</section>

<section class="subscribe">
  <div class="sub-title serif">SUBSCRIBE<br>NEWSLETTER</div>
  <svg style="position:absolute;left:78px;top:100px" width="52" height="40"><path d="M2 14l24-12 24 12v24H2z M2 14l24 16 24-16" fill="none" stroke="#2b4a66" stroke-width="2"/></svg>
  <p class="sub-text">Get a weekly round-up of the top cloud computing news and views form Kelvrim-IT and more to help you stay ahead and make informed decisions.</p>
  <div class="sub-form"><span class="field">Enter Your Name</span><span class="field">Enter Your Email</span><span class="sub-btn">SUBSCRIBE</span></div>
  <svg style="position:absolute;left:1065px;top:-22px" width="60" height="40"><path d="M4 36l40-30 8 6-40 30z" fill="none" stroke="#555" stroke-width="2"/></svg>
</section>

<section class="partners">
  <h2 class="serif">OUR TOP PARTNERS</h2>
  <div class="cards">
    <div class="card"><div class="photo" role="img" aria-label="Partner portrait photo"></div><dl><dd>Name : Anvika</dd><dd>Education : MBA</dd><dd>Companies Worked For : NA</dd><dd>Notes : NA</dd></dl></div>
    <div class="card"><div class="photo" role="img" aria-label="Partner portrait photo"></div><dl><dd>Name : Anvika</dd><dd>Education : MBA</dd><dd>Companies Worked For : NA</dd><dd>Notes : NA</dd></dl></div>
    <div class="card"><div class="photo" role="img" aria-label="Partner portrait photo"></div><dl><dd>Name : Anvika</dd><dd>Education : MBA</dd><dd>Companies Worked For : NA</dd><dd>Notes : NA</dd></dl></div>
    <div class="card"><div class="photo" role="img" aria-label="Partner portrait photo"></div><dl><dd>Name : Anvika</dd><dd>Education : MBA</dd><dd>Companies Worked For : NA</dd><dd>Notes : NA</dd></dl></div>
  </div>
  <div class="pager">
    <span><svg width="12" height="14"><path d="M10 1L2 7l8 6z" fill="#555"/></svg></span>
    <span><svg width="12" height="14"><path d="M2 1l8 6-8 6z" fill="#555"/></svg></span>
  </div>
</section>

<section class="talent">
  <h2 class="serif">TOP TALENT AT YOUR DISPOSAL</h2>
  <p>Lorem ipsum dolor sit amet, consectetuer adipiscing elit, sed diam nonummy nibh euismod tincidunt ut laoreet</p>
  <span class="btn-register"><svg width="24" height="18" viewBox="0 0 24 18"><path d="M2 9l6-6 4 3 4-3 6 6-8 7z" fill="none" stroke="#fff" stroke-width="2"/></svg>REGISTER AS A BUSINESS PARTNER</span>
</section>

<footer class="footer">
  <div class="fcol" style="left:73px"><h4>Industries</h4><ul><li>Financial Services</li><li>Retail</li><li>Nonprofit</li><li>Government</li><li>Life Sciences</li><li>Manufacturing</li><li>Healthcare</li><li>Real Estate</li><li>Communications</li><li>Higher Ed</li><li>Insurance</li></ul></div>
  <div class="fcol" style="left:217px"><h4>Project Category</h4><ul><li>Cloud Computing</li><li>QA Testing</li><li>Consulting Services</li><li>Web Development</li><li>Web Design</li><li>Security &amp; Compliance</li><li>Mobile App Development</li><li>Technical Support Services</li></ul></div>
  <div class="fcol" style="left:415px"><h4>Support &amp; Downloads</h4><ul><li>Support Team</li><li>Support Ticket</li><li>Help</li><li>FAQ</li><li>Downloads</li><li>Contact Us</li></ul><h4 style="margin-top:14px">Events</h4><ul><li>Latest</li><li>Career Events</li></ul></div>
  <div class="fcol" style="left:608px"><h4>Career</h4><ul><li>Internship</li><li>Career</li></ul><h4 style="margin-top:14px">Blog</h4><ul><li>Latest</li><li>Most Popular</li><li>Lists</li></ul></div>
  <div class="fsocial"><span class="dot"></span><span class="dot"></span><span class="dot"></span><span class="dot"></span></div>
  <div class="fcontact">
    <div><span class="ic"></span>Customer Service</div>
    <div><span class="ic"></span>info@kelvrim.example</div>
    <div><span class="ic"></span>02531478096</div>
  </div>
  <div class="flogo">Kelvrim</div>
  <div class="fbottom">© 2016 Kelvrim. All Rights Reserved. &nbsp;Terms of Use &nbsp;/ &nbsp;Privacy Policy</div>
</footer>

</body>
</html>
```